Guiding Your Revenue Overhaul *

Bold eye-catching design for business non-fiction: I am seeking a bold, and clean design for a book. The book will be 6X9 for both the ebook and in print. I am open to ideas, but found that books like “steady as rain” with contrast are highly desirable for business books.

I am open to color choices.

I would also like a growth orientated graphic in the book - something to show growth, leadership, movement. Not just a plain graphic.

The title:

Guiding Your Revenue Overhaul

The subtitle - I am open to suggestions. Two subtitles I am considering:

A framework for new sales leaders and those who want to keep winning.

A Roadmap for First-Time Sales Chiefs and Those Who Aim to Stay on Top.

The below is an introduction of the book: (Back Jacket)

Sales transformation is a topic that is infrequently written about. For the new sales leader, there are a myriad of books written on coaching, leadership, forecasting, solution selling and sales process but very little is written about how to assess a sales team and build a plan for long-term success.

Through my sales leadership career, whether recently promoted or starting with a new team, I have often asked the question: Where do I start?

In the end, I was disappointed with the answers from currently available books and research, left to figure it out myself - which I did over a decade, with great pain and through many transformations. The inability to answer the question – Where do I start? – is why I wrote this book. To answer that question.

The goal of this book is to help sales leaders answer that question by providing a framework to understand the business, build a plan, and guide the team through the different stages of a sales transformation. A framework to succeed at the fastest pace possible, quarter after quarter.

(End back jacket - the rest is just additional context)

Over the last decade, I have had the privilege of leading teams in North America, Europe, and Asia. I have led turnarounds, growth businesses, and realignments. Each team was different in size, complexity, and culture; and each one offered up new and unique challenges. Each team operated with different market dynamics: one was a commodity; one was a low-cost leader; one was a market innovator. Each transformation helped me learn by taking risks, by failing and by succeeding. At each step, I had many teachers; and as I learned, I made notes. Over time I built a framework that you can leverage as you read and absorb this book. As you lead your team through a sales transformation.

I hope that this book will become for you what The Copper Lantern is for me: a favorite on your bookshelf; underlined, highlighted, dog-eared, and an ongoing reference.

Sales leadership is a journey. It is never linear, and it is always changing. At different times, different parts of this book will apply, while others will not, but hopefully, you will find it a useful and long-lasting reference.

Target Market(s)

Business readers. Sales leaders.

Requirements
Must have
• Modern, clear, eye catching colours. Clean. Graphics that indicate growth, leadership, strength.
• Please ensure the design has the full cover and back jacket design. Please use the introduction of the book as the back jacket text.

```html
<!DOCTYPE html>
<html lang="en">
<head>
<meta charset="utf-8">
<title>Guiding Your Revenue Overhaul – Book Cover</title>
<link rel="stylesheet" href="https://fonts.googleapis.com/css2?family=Tinos:ital,wght@0,400;0,700;1,400&display=swap">
<style>
  :root {
    --page-bg-light: #eef2f4;
    --page-bg-dark: #cfd9de;
    --cover-red-core: #5c0005;
    --cover-red-edge: #2c0001;
    --gold-light: #f0c93a;
    --gold-mid: #d9a927;
    --gold-deep: #b9861f;
    --title-white: #ffffff;
    --author-ink: #3a0a06;
  }
  html, body {
    margin: 0;
    padding: 0;
    width: 1200px;
    height: 1200px;
    overflow: hidden;
  }
  body {
    background: radial-gradient(circle at 50% 45%, var(--page-bg-light) 0%, var(--page-bg-dark) 100%);
    font-family: "Tinos", "Times New Roman", serif;
  }
  .book-cover {
    position: absolute;
    left: 250px;
    top: 75px;
    width: 700px;
    height: 1050px;
    box-shadow: 0 6px 24px rgba(40, 50, 60, 0.25);
  }
  .book-cover svg {
    display: block;
    width: 100%;
    height: 100%;
  }
  .title-accent { font-family: "Tinos", "Times New Roman", serif; fill: var(--gold-mid); }
  .title-main { font-family: "Tinos", "Times New Roman", serif; fill: var(--title-white); }
  .title-strong { font-family: "Tinos", "Times New Roman", serif; font-weight: 700; fill: var(--title-white); }
  .subtitle { font-family: "Tinos", "Times New Roman", serif; font-style: italic; fill: var(--title-white); }
  .author-name { font-family: "Tinos", "Times New Roman", serif; fill: var(--author-ink); }
</style>
</head>
<body>
  <div class="book-cover">
    <svg viewBox="0 0 700 1050" xmlns="http://www.w3.org/2000/svg">
      <defs>
        <radialGradient id="coverRed" cx="50%" cy="45%" r="65%">
          <stop offset="0%" stop-color="var(--cover-red-core)"/>
          <stop offset="100%" stop-color="var(--cover-red-edge)"/>
        </radialGradient>
        <linearGradient id="goldSheen" x1="0" y1="0" x2="1" y2="1">
          <stop offset="0%" stop-color="var(--gold-deep)"/>
          <stop offset="50%" stop-color="var(--gold-light)"/>
          <stop offset="100%" stop-color="var(--gold-mid)"/>
        </linearGradient>
        <linearGradient id="goldBand" x1="0" y1="0" x2="1" y2="0">
          <stop offset="0%" stop-color="var(--gold-deep)"/>
          <stop offset="35%" stop-color="var(--gold-light)"/>
          <stop offset="65%" stop-color="var(--gold-mid)"/>
          <stop offset="100%" stop-color="var(--gold-light)"/>
        </linearGradient>
      </defs>

      <rect class="cover-field" x="0" y="0" width="700" height="1050" fill="url(#coverRed)"/>

      <path class="title-frame" d="M131 105 H82 V789 H613 V105 H287"
            fill="none" stroke="url(#goldSheen)" stroke-width="18"/>

      <text class="title-accent" x="334" y="258" font-size="125" text-anchor="middle">Guiding</text>
      <text class="title-main" x="100" y="419" font-size="36">Your</text>
      <text class="title-main" x="176" y="419" font-size="104">Revenue</text>
      <text class="title-strong" x="334" y="500" font-size="80" text-anchor="middle">Overhaul</text>

      <g class="subtitle" font-size="34" text-anchor="middle">
        <text x="330" y="575">A Roadmap for</text>
        <text x="330" y="623">First-Time Sales Chiefs</text>
        <text x="330" y="671">and Those Who Aim</text>
        <text x="330" y="719">to Stay on Top</text>
      </g>

      <rect class="author-band" x="0" y="940" width="700" height="110" fill="url(#goldBand)"/>
      <text class="author-name" x="350" y="1008" font-size="60" text-anchor="middle" letter-spacing="-2">AUTHOR NAME</text>
    </svg>
  </div>
</body>
</html>
```